Velvet Crest Car Detailing Brochure

I would like a trifold brochure designed for my car detailing business. The background has to be full black or mostly black with some designing using only colors present in our logo.

Front page must have our logo and name, list of services, a photo and mybe our phone number but no long text.

Inside I want to present each service one by one with its description and a photo representing/showing each service. (I will provide the text below). For photos, use stock photos and I will add come of mines already too.

On the back of the brochure I want to have contact & info: phone number, opening hours, address, website, Instagram.

Outside left I want the text About us and photo/design.

I want the brochure to be neat, professional, easy to read, but at the same time not too boring.

Text:
1. About us
a. the ultimate destination for car care in Geneva. We provide personalized, detail-oriented services that bring out the best in your car. With our expert techniques and dedicated approach, we ensure that your car receives the utmost care and attention. Experience a place where passion meets precision and let us create an exceptional car care experience designed just for you.
2. Services:

DETAILING & HAND WASH

• Comprehensive exterior & interior care
• Personalisation and tailored cleaning packages
• Decontamination
• Premium products
• Attention to detail for a perfect finish

POLISHING

• Eliminates scratches, holograms
• Revives and protects paint
• Ensures lasting gloss
• Enhances paint life
• Preserves car’s value and beauty

CERAMIC TREATMENT

• Durable paint protection
• Water-repellent (hydrophobic) effect
• Easier cleaning, enhanced shine
• Long-term surface safeguarding
• Shields against environmental impacts

DRY ICE WASH

• Innovative, waterless method
• Safe for all car parts
• Deep cleans, removes odors
• Allergen-free, antibacterial
• Gentle, effective
• Advanced cleaning technology

COVERING

• Personalized vehicle styling
• More than 150 colours available
• Clean cut without using a cutter
• High-quality, durable materials
• Custom designs available

PROTECTION FILM

• Invisible, durable shield
• Self-healing technology
• 10-year warranty by QR VONT

DETAILING BOUTIQUE

• Premium brands available
• Buy on site during your visit
• Marble Harbour, Zeb Autos, DRUP Polaro
• Essential for at-home car care
• Perfect for quick touch-ups
(for these three brands you can put their logos

Target Market(s)

Our target market includes car owners of all price ranges, with a special focus on those who are passionate about their vehicles. We cater to clients who value excellent service and results, and seek to maintain their cars in pristine condition.

Industry/Entity Type

Automobile / Car detailing

Colors

Designer to choose colors to be used in the design.

Requirements
Must have
• Brand Consistency: The brochure must adhere to our brand colors and style, particularly utilizing the colors present in our logo. Trifold Layout: The design must be specifically tailored for a trifold brochure format. Legibility: Text must be easy to read against the mostly black background, with appropriate font size and style. Professional Look and Feel: The overall design must convey professionalism while being engaging and not overly complex. Photo representation: each service description should have a phot presenting it.
Should not have
• Overcrowded Design: Avoid cluttering with too much text or too many images. The layout should be clean and easy to navigate. Cartoonish Fonts or Graphics: Avoid using unprofessional or casual fonts and graphics that do not align with the upscale and professional image of our business. Distracting Backgrounds: The background should complement and not overpower the content. Stick to the theme of mostly black with design elements from our logo.

```html
<!DOCTYPE html>
<html lang="en">
<head>
<meta charset="utf-8">
<title>Velvet Crest Car Detailing – Trifold Brochure</title>
<link href="https://fonts.googleapis.com/css2?family=Montserrat:wght@400;500;600;700;900&display=swap" rel="stylesheet">
<style>
:root{
  --pink:#e0479e;
  --purple:#8a4fc8;
  --blue:#4d7fd8;
  --black:#050505;
  --ink:#111;
  --white:#fff;
  --stage:#e4e4e4;
  --muted:#d8d8d8;
}
*{box-sizing:border-box;margin:0;padding:0}
html,body{width:1200px;height:892px;overflow:hidden;background:var(--stage);font-family:'Montserrat',sans-serif}
.spread-frame{position:absolute;top:218px;width:590px;height:456px;overflow:hidden;box-shadow:0 4px 14px rgba(0,0,0,.25)}
.spread-frame.inside{left:6px}
.spread-frame.outside{left:604px}
.spread{position:absolute;left:0;top:0;width:922px;height:712px;transform:scale(.64);transform-origin:0 0;background:var(--black);overflow:hidden;color:var(--white)}

/* ---------- inside ---------- */
.title-band{position:absolute;left:0;top:0;width:617px;height:66px;background:var(--white);overflow:hidden}
.title-band h1{position:absolute;left:18px;top:2px;font-size:76px;font-weight:900;letter-spacing:3px;color:var(--ink);line-height:1}
.sheen{position:absolute;left:0;width:617px;height:60px;background:linear-gradient(180deg,rgba(255,255,255,0),rgba(255,255,255,.07),rgba(255,255,255,0))}
.service{position:absolute;width:295px}
.service h2{font-size:11.5px;font-weight:700;color:var(--pink);letter-spacing:.2px;margin-bottom:5px}
.service ul{list-style:none;width:178px}
.service li{position:relative;padding-left:12px;font-size:10.2px;line-height:12.3px;margin-bottom:3.6px;color:#f1f1f1}
.service li::before{content:"\2713";position:absolute;left:0;top:0;color:var(--pink);font-size:9px}
.service .photo{position:absolute;right:0;top:0;width:104px;height:150px;border:1px solid #bbb}
.brands{margin-top:8px;margin-left:12px;font-size:11px;font-weight:700;line-height:16px;color:var(--white)}
.panel-photo{position:absolute;left:635px;top:0;width:266px;height:495px}

/* ---------- outside ---------- */
.flap-photo{position:absolute;left:0;top:0;width:305px;height:712px;background:linear-gradient(180deg,#4a4f56 0%,#2c2f33 40%,#0d0d0d 68%,#000 80%)}
.about{position:absolute;left:34px;top:462px;width:250px}
.about h2{font-size:34px;font-weight:400;background:linear-gradient(90deg,var(--pink),var(--purple));-webkit-background-clip:text;background-clip:text;color:transparent;margin-bottom:6px}
.about p{font-size:10.6px;line-height:16.3px;color:#eee}
.about strong{font-weight:700;color:var(--white)}
.lower-light{position:absolute;left:305px;top:430px;width:617px;height:282px;background:linear-gradient(180deg,#000 0%,#fff 28%,#fff 100%)}
.lower-light.front{left:617px;width:305px;background:linear-gradient(180deg,#000 0%,#666 20%,#ddd 45%,#fff 70%)}
.car-photo{position:absolute;left:305px;top:180px;width:617px;height:290px;background:radial-gradient(ellipse at 55% 55%,#3b3b3b 0%,#151515 45%,#000 75%)}
.hours{position:absolute;left:305px;top:62px;width:312px;text-align:center}
.hours h3{font-size:13px;font-weight:700;margin-bottom:22px}
.hours-cols{display:flex;justify-content:center;font-size:11.5px;line-height:21px;color:#ddd}
.hours-cols div{padding:0 14px}
.hours-cols div:first-child{border-right:1px solid #bbb}
.contact{position:absolute;left:305px;top:492px;width:312px;text-align:center;color:var(--ink);font-size:12.5px;line-height:15px}
.contact h3{font-size:13px;font-weight:700;margin-bottom:18px}
.contact p{margin-bottom:18px}
.brand-block{position:absolute;left:617px;top:38px;width:305px;text-align:center}
.brand-mark{width:92px;height:92px;border:4px solid var(--purple);border-radius:50%;margin:0 auto 18px}
.brand-name{font-size:19px;font-weight:500;letter-spacing:.6px;color:var(--white)}
.service-list{position:absolute;left:666px;top:488px;width:256px;list-style:none}
.service-list li{font-size:12.5px;font-weight:700;color:var(--ink);height:23.5px;padding-top:3px;border-bottom:1.5px solid var(--blue);position:relative;padding-left:18px;letter-spacing:.3px}
.service-list li::before{content:"\2713";position:absolute;left:2px;top:2px;font-size:12px}
.front-phone{position:absolute;left:668px;top:663px;display:flex;align-items:center;gap:8px;font-size:15px;font-weight:700;color:var(--pink)}
</style>
</head>
<body>

<!-- inside spread -->
<div class="spread-frame inside">
  <section class="spread" aria-label="Inside pages">
    <div class="title-band"><h1>SERVICES</h1></div>
    <div class="sheen" style="top:250px"></div>
    <div class="sheen" style="top:465px"></div>

    <div class="service" style="left:12px;top:102px">
      <h2>DETAILING &amp; HAND WASH</h2>
      <ul>
        <li>Comprehensive exterior &amp; interior care</li>
        <li>Personalisation and tailored cleaning packages</li>
        <li>Decontamination</li>
        <li>Premium products</li>
        <li>Attention to detail for a perfect finish</li>
      </ul>
      <div class="photo" role="img" aria-label="Wash mitt cleaning a car grille" style="background:linear-gradient(160deg,#8fa0b5,#3c4552 60%,#1c1f24)"></div>
    </div>

    <div class="service" style="left:12px;top:308px">
      <h2>DRY ICE WASH</h2>
      <ul>
        <li>Innovative, waterless method</li>
        <li>Safe for all car parts</li>
        <li>Deep cleans, removes odors</li>
        <li>Allergen-free, antibacterial</li>
        <li>Gentle, effective</li>
        <li>Advanced cleaning technology</li>
      </ul>
      <div class="photo" role="img" aria-label="Dry ice blasting machine" style="background:linear-gradient(160deg,#c9cfcf,#6f7875 55%,#2a2d2c)"></div>
    </div>

    <div class="service" style="left:12px;top:520px">
      <h2>CERAMIC TREATMENT</h2>
      <ul>
        <li>Durable paint protection</li>
        <li>Water-repellent (hydrophobic) effect</li>
        <li>Easier cleaning, enhanced shine</li>
        <li>Long-term surface safeguarding</li>
        <li>Shields against environmental impacts</li>
      </ul>
      <div class="photo" role="img" aria-label="Gloved hand applying ceramic coating to a red car" style="background:linear-gradient(160deg,#4e6c8e,#7a1e28 55%,#2a0c10)"></div>
    </div>

    <div class="service" style="left:322px;top:102px">
      <h2>POLISHING</h2>
      <ul>
        <li>Eliminates scratches, holograms</li>
        <li>Revives and protects paint</li>
        <li>Ensures lasting gloss</li>
        <li>Enhances paint life</li>
        <li>Preserves car’s value and beauty</li>
      </ul>
      <div class="photo" role="img" aria-label="Polishing machine on car paint" style="background:linear-gradient(160deg,#6a6f75,#2c3036 55%,#3aa0b0)"></div>
    </div>

    <div class="service" style="left:322px;top:308px">
      <h2>COVERING</h2>
      <ul>
        <li>Personalized vehicle styling</li>
        <li>More than 150 colours available</li>
        <li>Clean cut without using a cutter</li>
        <li>High-quality, durable materials</li>
        <li>Custom designs available</li>
      </ul>
      <div class="photo" role="img" aria-label="Installer applying purple wrap film to a car" style="background:linear-gradient(160deg,#8b8f96,#4a2d63 60%,#1a1020)"></div>
    </div>

    <div class="service" style="left:322px;top:520px">
      <h2>DETAILING BOUTIQUE</h2>
      <ul>
        <li>Premium brands available</li>
        <li>Buy on site during your visit</li>
        <li>Essential for at-home car care</li>
        <li>Perfect for quick touch-ups</li>
      </ul>
      <div class="brands">Marble Harbour<br>Zeb Autos<br>DRUP Polaro</div>
      <div class="photo" role="img" aria-label="Detailing brush cleaning a car interior" style="background:linear-gradient(160deg,#b7b7b7,#4b4b4b 55%,#1b1b1b)"></div>
    </div>

    <div class="panel-photo" role="img" aria-label="Machine polishing the side of a dark car" style="background:linear-gradient(170deg,#d8dde0 0%,#7b8288 30%,#3b3f45 60%,#1a1c1f 100%)"></div>

    <div class="service" style="left:632px;top:520px;width:270px">
      <h2>PROTECTION FILM</h2>
      <ul style="width:160px">
        <li>Invisible, durable shield</li>
        <li>Self-healing technology</li>
        <li>10-year warranty by QR VONT</li>
      </ul>
      <div class="photo" role="img" aria-label="Microfibre towels on a glossy car bonnet" style="background:linear-gradient(160deg,#b0b4b8,#3a3c40 50%,#e08a2a)"></div>
    </div>
  </section>
</div>

<!-- outside spread -->
<div class="spread-frame outside">
  <section class="spread" aria-label="Outside pages">
    <div class="flap-photo" role="img" aria-label="Polisher working on a car interior console"></div>
    <div class="about">
      <h2>About us</h2>
      <p>The <strong>ultimate destination for car care</strong> in Geneva. We provide personalized, detail-oriented services that bring out the best in your car. With our expert techniques and dedicated approach, we ensure that your car receives the utmost care and attention. Experience a place where passion meets precision and let us create an exceptional car care experience designed just for you.</p>
    </div>

    <div class="lower-light"></div>
    <div class="lower-light front"></div>
    <div class="car-photo" role="img" aria-label="Glossy black sports car"></div>

    <div class="hours">
      <h3>Opening Time Visit Us</h3>
      <div class="hours-cols">
        <div>Monday – Friday<br>8:00am – 5:00pm</div>
        <div>Saturday – Closed<br>Sunday – Closed</div>
      </div>
    </div>

    <div class="contact">
      <h3>Contact Us!</h3>
      <p>+41 22 555 0147</p>
      <p>St Name Here, 000<br>City Name, ES</p>
      <p>velvetcrest@email.com<br>@velvetcrest</p>
      <p>www.velvetcrest.com</p>
    </div>

    <div class="brand-block">
      <div class="brand-mark"></div>
      <div class="brand-name">VELVET CREST</div>
    </div>

    <ul class="service-list">
      <li>DETAILING &amp; HAND WASH</li>
      <li>POLISHING</li>
      <li>CERAMIC TREATMENT</li>
      <li>DRY ICE WASH</li>
      <li>COVERING</li>
      <li>PROTECTION FILM</li>
      <li>DETAILING BOUTIQUE</li>
    </ul>

    <div class="front-phone">
      <svg width="13" height="13" viewBox="0 0 24 24" aria-hidden="true"><path fill="#111" d="M6.6 10.8a15.1 15.1 0 0 0 6.6 6.6l2.2-2.2a1 1 0 0 1 1-.25 11.4 11.4 0 0 0 3.6.57 1 1 0 0 1 1 1V20a1 1 0 0 1-1 1A17 17 0 0 1 3 4a1 1 0 0 1 1-1h3.5a1 1 0 0 1 1 1c0 1.25.2 2.45.57 3.57a1 1 0 0 1-.25 1z"/></svg>
      <span>+41 22 555 0147</span>
    </div>
  </section>
</div>

</body>
</html>
```